NEW YORK Plumbing/utility company 10 year anniversary business card

Looking For simple back and front business card would like to include a few things in description
We offer 24/7 emergency service
residential
commercial
industrial
municipal
services offered
Plumbing
hydro excavation
hydro jetting
Well pumps
Sewer pumps
water mains
sewer mains

```html
<!DOCTYPE html>
<html lang="en">
<head>
<meta charset="utf-8">
<title>Ridgeline Water &amp; Sewer – Business Card</title>
<link href="https://fonts.googleapis.com/css2?family=Montserrat:wght@700&family=Arimo:wght@400;700&display=swap" rel="stylesheet">
<style>
  :root {
    --navy: #0a5f9e;
    --cyan: #1aaaf0;
    --white: #ffffff;
    --stage: #dcdcde;
    --brand-font: "Montserrat", sans-serif;
    --body-font: "Arimo", sans-serif;
  }
  html, body {
    margin: 0;
    width: 1200px;
    height: 1200px;
    overflow: hidden;
    background: var(--stage);
  }
  .card {
    position: absolute;
    left: 173px;
    width: 854px;
    height: 488px;
    overflow: hidden;
  }
  .card--front { top: 84px; background: var(--white); }
  .card--back { top: 628px; background: var(--navy); }

  .brand {
    position: absolute;
    left: 0;
    right: 0;
    top: 76px;
    text-align: center;
    font-family: var(--brand-font);
    font-weight: 700;
    color: var(--navy);
    line-height: 1;
  }
  .brand__main {
    display: block;
    font-size: 76px;
    letter-spacing: 4px;
  }
  .brand__sub {
    display: block;
    margin-top: 30px;
    font-size: 30px;
    letter-spacing: 5px;
  }
  .card--back .brand { color: var(--white); }

  .swoosh { position: absolute; left: 0; top: 0; }

  .contact {
    position: absolute;
    top: 370px;
    left: 0;
    right: 0;
    font-family: var(--body-font);
    color: var(--white);
  }
  .contact__person {
    position: absolute;
    right: 453px;
    top: 10px;
    text-align: right;
  }
  .contact__name {
    font-weight: 700;
    font-size: 25px;
    color: var(--cyan);
    letter-spacing: 0.5px;
  }
  .contact__role { font-size: 22px; margin-top: 4px; }
  .contact__divider {
    position: absolute;
    left: 426px;
    top: 12px;
    width: 2px;
    height: 55px;
    background: var(--white);
  }
  .contact__lines {
    position: absolute;
    left: 450px;
    top: 6px;
    font-size: 22px;
  }
  .contact__line {
    display: flex;
    align-items: center;
    gap: 12px;
    height: 34px;
  }
  .contact__line svg { width: 22px; height: 22px; }

  .offer {
    position: absolute;
    left: 0;
    right: 0;
    text-align: center;
    font-family: var(--body-font);
    color: var(--white);
  }
  .offer__headline {
    top: 278px;
    font-size: 23px;
    font-weight: 700;
  }
  .offer__headline span {
    padding: 2px 90px;
    background: radial-gradient(ellipse at center, rgba(26,170,240,0.55), rgba(26,170,240,0) 70%);
  }
  .bullets {
    font-size: 23px;
  }
  .bullets span::before {
    content: "";
    display: inline-block;
    width: 9px;
    height: 9px;
    border-radius: 50%;
    background: var(--cyan);
    margin: 0 8px 4px 16px;
  }
  .offer__markets { top: 315px; }
  .offer__title {
    top: 366px;
    font-size: 23px;
    font-weight: 700;
  }
  .offer__title span {
    padding: 4px 60px;
    background: linear-gradient(90deg, rgba(26,170,240,0), rgba(26,170,240,0.5) 30%, rgba(26,170,240,0.5) 70%, rgba(26,170,240,0));
  }
  .offer__services-1 { top: 403px; }
  .offer__services-2 { top: 430px; }
</style>
</head>
<body>

<section class="card card--front">
  <div class="brand">
    <span class="brand__main">RIDGELINE</span>
    <span class="brand__sub">WATER &amp; SEWER</span>
  </div>

  <svg class="swoosh" width="854" height="488" viewBox="0 0 854 488" aria-hidden="true">
    <path fill="var(--cyan)" d="M171,310 Q560,278 854,334 L854,352 Q560,292 171,310 Z"/>
    <path fill="var(--navy)" d="M0,334 Q430,284 854,352 L854,366 Q760,342 659,334 Q300,322 0,358 Z"/>
    <path fill="var(--navy)" d="M0,374 Q330,328 659,336 Q760,344 854,370 V488 H0 Z"/>
  </svg>

  <div class="contact">
    <div class="contact__person">
      <div class="contact__name">DANIEL ORTIZ</div>
      <div class="contact__role">Manager</div>
    </div>
    <div class="contact__divider"></div>
    <div class="contact__lines">
      <div class="contact__line">
        <svg viewBox="0 0 24 24" aria-hidden="true"><path fill="var(--cyan)" d="M6.6 10.8a15.1 15.1 0 0 0 6.6 6.6l2.2-2.2c.3-.3.7-.4 1-.2 1.1.4 2.3.6 3.6.6.6 0 1 .4 1 1V20c0 .6-.4 1-1 1A17 17 0 0 1 3 4c0-.6.4-1 1-1h3.5c.6 0 1 .4 1 1 0 1.3.2 2.5.6 3.6.1.3 0 .7-.2 1z"/></svg>
        <span>845-555-0182</span>
      </div>
      <div class="contact__line">
        <svg viewBox="0 0 24 24" aria-hidden="true"><path fill="var(--cyan)" d="M2 5h20v14H2z"/><path fill="none" stroke="var(--navy)" stroke-width="1.6" d="M2 5l10 8 10-8M2 19l7-7M22 19l-7-7"/></svg>
        <span>info@ridgelinews.com</span>
      </div>
    </div>
  </div>
</section>

<section class="card card--back">
  <div class="brand">
    <span class="brand__main">RIDGELINE</span>
    <span class="brand__sub">WATER &amp; SEWER</span>
  </div>

  <div class="offer offer__headline"><span>We offer 24/7 emergency service</span></div>
  <div class="offer bullets offer__markets">
    <span>Residential</span><span>Commercial</span><span>Industrial</span><span>Municipal</span>
  </div>
  <div class="offer offer__title"><span>Services Offered</span></div>
  <div class="offer bullets offer__services-1">
    <span>Plumbing</span><span>hydro excavation</span><span>hydro jetting</span>
  </div>
  <div class="offer bullets offer__services-2">
    <span>Well pumps</span><span>Sewer pumps</span><span>water mains</span><span>sewer mains</span>
  </div>
</section>

</body>
</html>
```